SkyvoraQ Business Cards and Stationary Design

Need a design for our business cards and stationary. I want to carry on the theme of the logo. I want the business cards to have a design on the back. I would like the business cards and the stationary to carry the same theme, design scheme, and branding

Target Market(s)

Airlines and Maintenance Facilities

Industry/Entity Type

Aviation

Contact Information for Business Card

Name
Position Title
Address: 4827 Tollbeck Lane, Fort Pierce, Florida, 34951
Office Number
Mobile Number
Email
Website

Font styles to use
Serif
Sans Serif

Colors

Designer to choose colors to be used in the design.

```html
<!DOCTYPE html>
<html lang="en">
<head>
<meta charset="utf-8">
<title>SkyvoraQ Business Card</title>
<link href="https://fonts.googleapis.com/css2?family=Roboto:wght@400;500;700&display=swap" rel="stylesheet">
<style>
  :root {
    --backdrop: #dedede;
    --navy: #0b2850;
    --sky: #1a8fd6;
    --sky-deep: #0d5ea8;
    --paper: #f2f2f2;
    --white: #ffffff;
  }
  * { margin: 0; padding: 0; box-sizing: border-box; }
  html, body {
    width: 1200px; height: 960px; overflow: hidden;
    background: var(--backdrop);
    font-family: "Roboto", Arial, sans-serif;
  }
  .canvas { position: relative; width: 1200px; height: 960px; }
  .card {
    position: absolute; width: 600px; height: 342px; overflow: hidden;
    box-shadow: 2px 3px 4px rgba(0,0,0,0.35);
  }
  .card--front { left: 315px; top: 113px; background: var(--paper); }
  .card--back { left: 312px; top: 472px; background: var(--navy); }
  .front-sweep, .back-mark { position: absolute; inset: 0; }

  .brand { position: absolute; left: 37px; top: 37px; width: 225px; text-align: center; }
  .brand-dot {
    display: block; width: 72px; height: 72px; margin: 0 auto 19px;
    border-radius: 50%; background: var(--sky-deep);
  }
  .brand-name {
    display: block; color: var(--navy); font-weight: 700;
    font-size: 25px; letter-spacing: 4.5px; line-height: 1;
  }

  .contact {
    position: absolute; right: 40px; top: 145px;
    color: var(--white); text-align: right;
  }
  .contact-name { font-size: 21px; font-weight: 500; line-height: 1.1; }
  .contact-role { font-size: 15px; font-weight: 400; line-height: 1.2; margin-top: 1px; }
  .contact-address { font-size: 14.5px; line-height: 18px; margin-top: 9px; }
  .contact-lines { list-style: none; margin-top: 7px; font-size: 14.5px; }
  .contact-lines li { display: flex; justify-content: flex-end; align-items: center; height: 19.5px; }
  .contact-lines svg { width: 14px; height: 14px; margin-left: 8px; fill: var(--white); }

  .back-brand { position: absolute; left: 31px; top: 278px; color: var(--white); }
  .back-name { display: block; font-size: 25px; font-weight: 700; letter-spacing: 4.5px; line-height: 1; }
  .back-url { display: block; font-size: 13px; letter-spacing: 3.4px; margin-top: 6px; }
</style>
</head>
<body>
<main class="canvas">
  <section class="card card--front" aria-label="Business card front">
    <svg class="front-sweep" viewBox="0 0 600 342" width="600" height="342" aria-hidden="true">
      <defs>
        <linearGradient id="sweepGlow" x1="0" y1="1" x2="1" y2="0">
          <stop offset="0" stop-color="var(--sky-deep)"/>
          <stop offset="0.5" stop-color="var(--sky)"/>
          <stop offset="1" stop-color="var(--sky-deep)"/>
        </linearGradient>
      </defs>
      <path d="M95 342 C200 215 400 60 600 0 L600 342 Z" fill="url(#sweepGlow)"/>
      <path d="M152 342 C250 225 420 85 600 0 L600 342 Z" fill="var(--navy)"/>
    </svg>

    <div class="brand">
      <span class="brand-dot"></span>
      <span class="brand-name">SKYVORAQ</span>
    </div>

    <div class="contact">
      <p class="contact-name">MARCUS DELANEY</p>
      <p class="contact-role">CEO/FOUNDER</p>
      <p class="contact-address">4827 Tollbeck Lane<br>Fort Pierce, Florida, 34951</p>
      <ul class="contact-lines">
        <li>689 512 7704
          <svg viewBox="0 0 24 24" aria-hidden="true"><path d="M6.6 10.8a15.1 15.1 0 0 0 6.6 6.6l2.2-2.2a1 1 0 0 1 1-.25 11.4 11.4 0 0 0 3.6.57 1 1 0 0 1 1 1V20a1 1 0 0 1-1 1A17 17 0 0 1 3 4a1 1 0 0 1 1-1h3.5a1 1 0 0 1 1 1c0 1.25.2 2.45.57 3.57a1 1 0 0 1-.25 1z"/></svg>
        </li>
        <li>836 291 4057
          <svg viewBox="0 0 24 24" aria-hidden="true"><path d="M7 1h10a2 2 0 0 1 2 2v18a2 2 0 0 1-2 2H7a2 2 0 0 1-2-2V3a2 2 0 0 1 2-2zm0 3v15h10V4zm5 16.2a1 1 0 1 0 0 .01z"/></svg>
        </li>
        <li>info@skyvoraq.com
          <svg viewBox="0 0 24 24" aria-hidden="true"><path d="M2 5h20v14H2zm2 2v.5l8 5 8-5V7zm0 2.8V17h16V9.8l-8 5z"/></svg>
        </li>
        <li>www.skyvoraq.com
          <svg viewBox="0 0 24 24" aria-hidden="true"><path d="M12 2a10 10 0 1 0 0 20 10 10 0 0 0 0-20zm-1 17.9A8 8 0 0 1 4.2 10L9 14.8v1a2 2 0 0 0 2 2zm6.9-2.5A2 2 0 0 0 16 16h-1v-3a1 1 0 0 0-1-1H8v-2h2a1 1 0 0 0 1-1V7h2a2 2 0 0 0 2-2v-.4a8 8 0 0 1 2.9 12.8z"/></svg>
        </li>
      </ul>
    </div>
  </section>

  <section class="card card--back" aria-label="Business card back">
    <svg class="back-mark" viewBox="0 0 600 342" width="600" height="342" role="img" aria-label="Large brand mark area">
      <circle cx="453" cy="188" r="188" fill="var(--white)"/>
    </svg>
    <div class="back-brand">
      <span class="back-name">SKYVORAQ</span>
      <span class="back-url">www.skyvoraq.com</span>
    </div>
  </section>
</main>
</body>
</html>
```